(6) High-Impact Facebook/Instagram Meta Ads Stills for joyCIRRUS Helicopter Tours

**DO NOT SUBMIT AI-GENERATED DESIGNS**
joyCIRRUS (www.joycirrus.com) is a premium helicopter tour company offering scenic flights over Tampa, St. Petersburg, and Sarasota. Our brand focuses on adventure, romance, and unforgettable aerial experiences. We want to elevate our Meta Ads creative with a set of scroll stopping still images that match the quality and emotional impact of our video content.
________________________________________
Project Goal
Create 6 Meta Ads stills that are visually striking, emotionally engaging, and optimized for performance on Facebook & Instagram. These stills will be used in both prospecting and retargeting campaigns.
The goal is to:
• Stop the scroll
• Communicate the experience instantly
• Highlight our offer
• Reinforce trust and social proof
• Match the look and feel of modern, high performing Meta ads
• Must match our brand colors (visit our website for colors)
What You Will Design (6 Total Stills)
We need six distinct still ads, each with a different angle and purpose. You may have to photoshop the red helicopter or Feet POV views into different scenes to make them more appealing!! Here are some general ideas, but we’re also open for your input:

1. Scenic Beauty Still
• Aerial coastline, beaches, bridges, or skyline
• Text overlay example: “See Tampa & St Pete Like Never Before”

2. POV / Cockpit Experience Still
• Inside the helicopter, Feet POV, showing the view or passengers
• Text overlay example: “Your Next Adventure Starts Here”

3. Romance / Date Night Still
• Couple in the helicopter, champagne, sunset, or emotional moment
• Text overlay example: “Florida Looks Better From Up Here”

4. Group Fun / Social Experience Still
• Friends smiling, reactions, excitement
• Text overlay example: “You’ve Never Seen Tampa & St Pete Like This”
• Price Anchor: “From $89 — Limited Time”

5. Offer Driven Still
• Clean, bold, easy to read
• Should clearly highlight our pricing
• Text overlay example: “From $89 — Limited Time”

6. Social Proof Still
• Strong trust building message
• Text overlay examples:
“★★★★★ Top Rated Helicopter Tours”
“Over 2,000 Happy Flyers”
“Florida’s #1 Helicopter Experience”
Design Requirements
Format & Specs
• Size: 1080x1350 (4:5 ratio) — Meta’s best performing format
• High resolution
• Clean, modern, premium look
• Must be easy to read on mobile
• Avoid clutter or too much text
• Bright, clean, adventurous
• Premium but approachable
• DO NOT USE ANY AI‑GENERATED IMAGES!
• Please use only the footage provided in the Google Drive folder. You may Photoshop or overlay the red helicopter (real image, not AI) from the Google Drive folder as needed.

Text Overlay Guidelines
• Use bold, easy to read fonts
• Keep text short and punchy
• Ensure high contrast for readability
• Place text in areas that don’t block key visuals

Logo
• Include the joyCIRRUS logo subtly (not overpowering)
Footage (Google Drive Folder):
https://files.qorbelvault.net/share/8KpR-TnWqLodHs3Yubfa29?mode=view

Logo (Google Drive Folder):
https://files.qorbelvault.net/share/4GmaT7XcepwoRbnLiqz2Vh?mode=link
Deliverables
• 6 final still ads (JPG or PNG)
• Editable source files (PSD, AI, or layered format)
• Consistent visual style across all 6 ads
Examples of Text You Can Use
(Choose whichever fits the image best)
• See Tampa & St Pete Like Never Before
• You’ve Never Seen Tampa & St Pete Like This
• Florida Looks Better From Up Here
• Your Next Adventure Starts Here
• This Is What Freedom Feels Like
• From $89 — Limited Time
• Top Rated Tours From $89
• ★★★★★ Top Rated Helicopter Tours
• Over 2,000 Happy Flyers
• Florida’s #1 Helicopter Experience

Tourism

Tourism, Aviation

• Must have our brand colors

```html
<!DOCTYPE html>
<html lang="en">
<head>
<meta charset="utf-8">
<title>joyCIRRUS Meta Ad Stills</title>
<link rel="stylesheet" href="https://fonts.googleapis.com/css2?family=Anton&family=Kaushan+Script&family=Montserrat:wght@500;600;700;800&family=Oswald:wght@500;600;700&display=swap">
<style>
:root{
  --orange:#f26a1b;
  --orange-deep:#e4571a;
  --navy:#1d3f6b;
  --navy-deep:#142c4d;
  --navy-glass:rgba(20,44,77,.86);
  --white:#ffffff;
  --ink:#1a2233;
  --page:#ffffff;
}
*{box-sizing:border-box;margin:0;padding:0}
html,body{width:1200px;height:1030px;overflow:hidden;background:var(--page)}
.board{position:relative;width:1200px;height:1030px}
.ad{position:absolute;width:355px;height:443px;overflow:hidden;box-shadow:0 2px 6px rgba(0,0,0,.25);font-family:"Montserrat",sans-serif;color:var(--white)}
.ad--scenic{left:34px;top:49px}
.ad--pov{left:424px;top:49px}
.ad--romance{left:813px;top:49px}
.ad--group{left:34px;top:529px}
.ad--offer{left:424px;top:529px}
.ad--proof{left:813px;top:529px}
.photo{position:absolute;inset:0}
.brand{position:absolute;top:16px;display:flex;align-items:center;gap:5px;font-family:"Montserrat",sans-serif;font-weight:700;font-size:10px;color:var(--white);letter-spacing:.3px}
.brand i{display:block;width:12px;height:12px;border-radius:50%;background:var(--white)}
.brand--left{left:20px}.brand--right{right:18px}
.head{position:absolute;left:24px;font-family:"Anton",sans-serif;line-height:.92;text-transform:uppercase;text-shadow:0 2px 6px rgba(0,0,0,.35)}
.orange{color:var(--orange)}
.script{font-family:"Kaushan Script",cursive;text-transform:none}
.bar{position:absolute;left:0;right:0;bottom:0;background:var(--navy);border-bottom:4px solid var(--orange);display:flex;align-items:center;justify-content:space-around;padding:0 10px}
.feat{display:flex;align-items:center;gap:6px;font-size:6.5px;font-weight:700;text-transform:uppercase;line-height:1.3}
.feat small{display:block;font-weight:500;font-size:6px}
.feat svg{width:14px;height:14px;flex:none;color:var(--white)}
.feat--o svg{color:var(--orange)}
.sep{width:1px;height:20px;background:rgba(255,255,255,.35)}
.locs{display:flex;align-items:center;gap:7px;font-size:7px;font-weight:600;letter-spacing:.4px;text-transform:uppercase}
.locs b{color:var(--orange);font-weight:600}
.locs svg{width:9px;height:9px;color:var(--orange)}
.ico{display:none}
</style>
</head>
<body>
<svg class="ico" aria-hidden="true">
  <symbol id="i-pin" viewBox="0 0 24 24"><path fill="currentColor" d="M12 2a7 7 0 0 0-7 7c0 5 7 13 7 13s7-8 7-13a7 7 0 0 0-7-7zm0 9.5A2.5 2.5 0 1 1 12 6.5a2.5 2.5 0 0 1 0 5z"/></symbol>
  <symbol id="i-shield" viewBox="0 0 24 24"><path fill="none" stroke="currentColor" stroke-width="2" d="M12 2l8 3v6c0 5-3.5 9-8 11-4.5-2-8-6-8-11V5z"/><path fill="none" stroke="currentColor" stroke-width="2" d="M8 12l3 3 5-6"/></symbol>
  <symbol id="i-camera" viewBox="0 0 24 24"><path fill="none" stroke="currentColor" stroke-width="2" d="M3 7h4l2-3h6l2 3h4v13H3z"/><circle cx="12" cy="13" r="4" fill="none" stroke="currentColor" stroke-width="2"/></symbol>
  <symbol id="i-heart" viewBox="0 0 24 24"><path fill="none" stroke="currentColor" stroke-width="2" d="M12 21s-8-5.5-8-11a4.5 4.5 0 0 1 8-3 4.5 4.5 0 0 1 8 3c0 5.5-8 11-8 11z"/></symbol>
  <symbol id="i-headset" viewBox="0 0 24 24"><path fill="none" stroke="currentColor" stroke-width="2" d="M4 15v-3a8 8 0 0 1 16 0v3"/><rect x="3" y="14" width="4" height="6" rx="1" fill="currentColor"/><rect x="17" y="14" width="4" height="6" rx="1" fill="currentColor"/></symbol>
  <symbol id="i-glasses" viewBox="0 0 24 24"><path fill="none" stroke="currentColor" stroke-width="2" d="M6 3h4l-1 7a2 2 0 0 1-2 0zM14 3h4l-1 7a2 2 0 0 1-2 0zM8 10v9M16 10v9M5 20h6M13 20h6"/></symbol>
  <symbol id="i-group" viewBox="0 0 24 24"><circle cx="7" cy="8" r="3" fill="none" stroke="currentColor" stroke-width="2"/><circle cx="17" cy="8" r="3" fill="none" stroke="currentColor" stroke-width="2"/><circle cx="12" cy="11" r="3" fill="none" stroke="currentColor" stroke-width="2"/><path fill="none" stroke="currentColor" stroke-width="2" d="M2 19c0-3 2-5 5-5M22 19c0-3-2-5-5-5M6 21c0-3 3-5 6-5s6 2 6 5"/></symbol>
  <symbol id="i-thumb" viewBox="0 0 24 24"><path fill="none" stroke="currentColor" stroke-width="2" d="M7 10v11H3V10zM7 10l4-8c2 0 3 1 3 3v4h6l-2 12H7"/></symbol>
  <symbol id="i-cal" viewBox="0 0 24 24"><rect x="3" y="5" width="18" height="16" rx="2" fill="none" stroke="currentColor" stroke-width="2"/><path stroke="currentColor" stroke-width="2" d="M3 10h18M8 3v4M16 3v4"/></symbol>
  <symbol id="i-clock" viewBox="0 0 24 24"><circle cx="12" cy="12" r="9" fill="none" stroke="currentColor" stroke-width="2.4"/><path fill="none" stroke="currentColor" stroke-width="2.4" d="M12 7v5l3 2"/></symbol>
  <symbol id="i-star" viewBox="0 0 24 24"><path fill="currentColor" d="M12 2l3 7 7 .6-5.3 4.7 1.6 7.2L12 17.8 5.7 21.5l1.6-7.2L2 9.6 9 9z"/></symbol>
</svg>

<main class="board">

  <!-- Ad 1: scenic -->
  <section class="ad ad--scenic">
    <div class="photo" role="img" aria-label="Aerial view of a turquoise beach coastline with high-rise towers and a red helicopter flying overhead" style="background:linear-gradient(180deg,#c9dbe9 0%,#8fb2c4 14%,#5f8a7a 30%,#4c7e5f 45%,#2ab7aa 70%,#1fa7a0 100%)"></div>
    <div class="brand brand--left"><i></i>joyCIRRUS</div>
    <div class="head" style="top:165px;font-size:40px">See</div>
    <div class="head" style="top:207px;font-size:72px">Tampa</div>
    <div class="head" style="top:280px;font-size:72px">&amp; St Pete</div>
    <div class="head orange" style="top:355px;font-size:38px">Like Never Before</div>
    <div class="locs" style="position:absolute;left:26px;top:400px"><svg><use href="#i-pin"/></svg>Tampa <b>|</b> St Petersburg <b>|</b> Sarasota</div>
    <div class="bar" style="height:30px">
      <div class="feat"><svg><use href="#i-camera"/></svg>Breathtaking views</div>
      <div class="feat"><svg><use href="#i-headset"/></svg>Expert pilots</div>
      <div class="feat"><svg><use href="#i-shield"/></svg>Safe &amp; reliable</div>
    </div>
  </section>

  <!-- Ad 2: POV -->
  <section class="ad ad--pov">
    <div class="photo" role="img" aria-label="Feet-out point of view from a helicopter above islands, beach towers and clear shallow water" style="background:linear-gradient(180deg,#9fc3dc 0%,#3f7aa0 12%,#5e7d5b 28%,#a8aca3 45%,#5fc6bc 65%,#2aa89e 100%)"></div>
    <div class="brand brand--left"><i></i>joyCIRRUS</div>
    <div class="head" style="top:145px;font-size:50px">Your Next</div>
    <div class="head orange" style="top:193px;font-size:50px">Adventure</div>
    <div class="head script" style="top:242px;left:20px;font-size:34px;color:var(--white)">Starts Here</div>
    <svg style="position:absolute;left:40px;top:280px" width="150" height="14" aria-hidden="true"><path d="M2 10 Q70 2 148 4" stroke="var(--orange)" stroke-width="3" fill="none"/></svg>
    <div style="position:absolute;left:20px;top:302px;display:flex;gap:5px;font-size:6px;font-weight:700;line-height:1.45;text-transform:uppercase">
      <svg width="9" height="11" style="color:var(--orange)"><use href="#i-pin"/></svg>
      <div>See Tampa, St Pete<br>&amp; Sarasota from<br><span class="orange">A whole new perspective</span></div>
    </div>
    <div class="bar" style="height:47px">
      <div class="feat feat--o"><svg><use href="#i-camera"/></svg><div>Unforgettable<br>views</div></div>
      <span class="sep"></span>
      <div class="feat feat--o"><svg><use href="#i-headset"/></svg><div>Expert<br>pilots</div></div>
      <span class="sep"></span>
      <div class="feat feat--o"><svg><use href="#i-shield"/></svg><div>Safe, smooth<br>&amp; reliable</div></div>
    </div>
  </section>

  <!-- Ad 3: romance -->
  <section class="ad ad--romance">
    <div class="photo" role="img" aria-label="Couple with headsets toasting champagne inside a helicopter above a riverside city at sunset" style="background:linear-gradient(180deg,#e7792e 0%,#7b4a3a 18%,#3c3f4a 40%,#2e3c52 70%,#1d2b42 100%)"></div>
    <div class="brand brand--right"><i></i>joyCIRRUS</div>
    <div class="head" style="top:40px;left:20px;font-size:66px">Florida</div>
    <div class="head script orange" style="top:100px;left:18px;font-size:38px">Looks Better</div>
    <div class="head" style="top:145px;left:20px;font-size:38px">From Up Here</div>
    <svg style="position:absolute;left:20px;top:180px" width="160" height="16" aria-hidden="true"><path d="M2 12 Q60 4 96 8" stroke="var(--orange)" stroke-width="3" fill="none"/><path d="M100 8 C96 2 92 4 95 8 L100 13 L105 8 C108 4 104 2 100 8" stroke="var(--orange)" stroke-width="1.5" fill="none"/><path d="M106 8 Q130 6 158 4" stroke="var(--orange)" stroke-width="2" fill="none"/></svg>
    <div style="position:absolute;left:20px;top:212px;font-size:7.5px;font-weight:700;line-height:1.5;text-transform:uppercase">The perfect view<br><span class="orange">For your perfect moment</span></div>
    <div style="position:absolute;left:26px;top:344px;width:303px;height:40px;border-radius:4px;background:rgba(30,40,60,.8);border:1px solid rgba(255,255,255,.2);display:flex;align-items:center;justify-content:space-around">
      <div class="feat feat--o"><svg><use href="#i-heart"/></svg><div>Romantic<br>experience</div></div><span class="sep"></span>
      <div class="feat feat--o"><svg><use href="#i-glasses"/></svg><div>Breathtaking<br>views</div></div><span class="sep"></span>
      <div class="feat feat--o"><svg><use href="#i-camera"/></svg><div>Memories that<br>last forever</div></div>
    </div>
    <div style="position:absolute;left:0;right:0;bottom:0;height:46px;background:var(--navy-deep);border-top:1px solid var(--orange);display:flex;align-items:center;justify-content:space-between;padding:0 18px">
      <div class="locs" style="font-size:6.5px"><svg><use href="#i-pin"/></svg>Tampa <b>|</b> St Petersburg <b>|</b> Sarasota</div>
      <div style="display:flex;align-items:center;gap:6px;border:1px solid var(--orange);border-radius:3px;padding:5px 7px;font-size:6px;font-weight:700;text-transform:uppercase;line-height:1.4">
        <svg width="14" height="14" style="color:var(--orange)"><use href="#i-cal"/></svg><div>Book your romantic flight<br><span class="orange" style="font-size:7px">Today ♥</span></div>
      </div>
    </div>
  </section>

  <!-- Ad 4: group -->
  <section class="ad ad--group">
    <div class="photo" role="img" aria-label="Smiling friends with headsets taking a selfie inside a helicopter above waterfront homes and palm trees" style="background:linear-gradient(160deg,#5d7a5a 0%,#d7c9a9 30%,#7a7f86 45%,#3c4a6a 65%,#5fbfb3 85%,#2fa39b 100%)"></div>
    <div class="brand brand--right"><i></i>joyCIRRUS</div>
    <div class="head" style="top:30px;left:20px;font-size:54px">Florida</div>
    <div class="head orange" style="top:82px;left:20px;font-size:54px">Looks Better</div>
    <div class="head script" style="top:138px;left:22px;font-size:28px;color:var(--white)">From Up Here</div>
    <svg style="position:absolute;left:40px;top:170px" width="140" height="10" aria-hidden="true"><path d="M2 8 Q70 2 138 3" stroke="var(--orange)" stroke-width="2.5" fill="none"/></svg>
    <div style="position:absolute;left:22px;top:224px;width:80px;color:var(--navy-deep)">
      <div class="feat feat--o" style="padding-bottom:8px;border-bottom:1px solid var(--orange)"><svg><use href="#i-heart"/></svg><div>Romantic<br>experience</div></div>
      <div class="feat feat--o" style="padding:8px 0;border-bottom:1px solid var(--orange)"><svg><use href="#i-glasses"/></svg><div>Champagne<br>toast</div></div>
      <div class="feat feat--o" style="padding-top:8px"><svg><use href="#i-camera"/></svg><div>Unforgettable<br>memories</div></div>
    </div>
    <div style="position:absolute;left:30px;top:322px;width:180px;height:52px;background:var(--navy);border-radius:26px 6px 26px 6px;display:flex;align-items:center;gap:8px;padding-left:14px">
      <svg width="20" height="20" style="color:var(--orange)"><use href="#i-heart"/></svg>
      <div><div style="font-family:'Oswald',sans-serif;font-weight:600;font-size:12px;text-transform:uppercase">Perfect for</div>
      <div class="script orange" style="font-size:9.5px;line-height:1.3">Date Nights, Anniversaries<br>&amp; Special Moments</div></div>
    </div>
    <div class="bar" style="height:58px">
      <div class="feat feat--o"><svg><use href="#i-shield"/></svg><div>Safe &amp; reliable<small>FAA certified</small></div></div><span class="sep"></span>
      <div class="feat feat--o"><svg><use href="#i-headset"/></svg><div>Expert pilots<small>Smooth rides</small></div></div><span class="sep"></span>
      <div class="feat feat--o"><svg><use href="#i-camera"/></svg><div>Breathtaking<small>views</small></div></div>
    </div>
  </section>

  <!-- Ad 5: offer -->
  <section class="ad ad--offer">
    <div class="photo" role="img" aria-label="Three excited passengers with headsets inside a helicopter above downtown Tampa and the convention center" style="background:linear-gradient(170deg,#6b6f78 0%,#8a7e78 25%,#4d5a6c 50%,#7a8391 70%,#1f3556 100%)"></div>
    <div class="brand brand--right"><i></i>joyCIRRUS</div>
    <div class="head" style="top:58px;left:18px;font-size:28px">You’ve Never Seen</div>
    <div class="head orange" style="top:88px;left:18px;font-size:54px">Tampa &amp;</div>
    <div class="head orange" style="top:140px;left:18px;font-size:54px">St Pete</div>
    <div class="head script" style="top:192px;left:18px;font-size:28px;color:var(--white)">Like This!</div>
    <div style="position:absolute;left:22px;top:245px;width:115px;height:100px;background:var(--orange-deep);transform:rotate(-3deg);border-radius:4px;text-align:center;padding-top:6px">
      <div style="font-family:'Anton',sans-serif;font-size:14px">FROM</div>
      <div style="font-family:'Anton',sans-serif;font-size:54px;line-height:.9"><sup style="font-size:24px">$</sup>89</div>
      <div style="margin:6px auto 0;width:104px;background:var(--navy-deep);font-family:'Oswald',sans-serif;font-weight:600;font-size:8.5px;padding:3px 0;display:flex;gap:4px;justify-content:center;align-items:center;color:var(--orange)"><svg width="9" height="9"><use href="#i-clock"/></svg>LIMITED TIME ONLY!</div>
    </div>
    <div style="position:absolute;left:0;right:0;top:362px;height:81px;background:var(--navy)">
      <div style="display:flex;justify-content:space-around;align-items:center;height:44px;padding:0 8px">
        <div class="feat feat--o"><svg><use href="#i-group"/></svg><div>Perfect for<br>groups</div></div><span class="sep"></span>
        <div class="feat feat--o"><svg><use href="#i-camera"/></svg><div>Unforgettable<br>memories</div></div><span class="sep"></span>
        <div class="feat feat--o"><svg><use href="#i-headset"/></svg><div>Expert pilots<br>safe &amp; reliable</div></div>
      </div>
      <div class="locs" style="justify-content:center;margin:4px 10px 0;background:var(--navy-deep);height:22px;font-size:8.5px;gap:12px"><svg style="width:10px;height:10px;color:var(--white)"><use href="#i-pin"/></svg>Tampa <b>|</b> St Petersburg <b>|</b> Sarasota</div>
    </div>
  </section>

  <!-- Ad 6: social proof -->
  <section class="ad ad--proof">
    <div class="photo" role="img" aria-label="Golden hour aerial skyline of downtown Tampa along the river and bay" style="background:linear-gradient(180deg,#f0b36a 0%,#c9885a 14%,#5c6374 30%,#3a4e6a 55%,#22395e 80%,#16294a 100%)"></div>
    <div class="brand brand--left"><i></i>joyCIRRUS</div>
    <div style="position:absolute;left:68px;top:68px;display:flex;gap:13px;color:var(--orange)">
      <svg width="30" height="30"><use href="#i-star"/></svg><svg width="30" height="30"><use href="#i-star"/></svg><svg width="30" height="30"><use href="#i-star"/></svg><svg width="30" height="30"><use href="#i-star"/></svg><svg width="30" height="30"><use href="#i-star"/></svg>
    </div>
    <div class="head" style="top:102px;left:0;right:0;text-align:center;font-size:88px">Top Rated</div>
    <div class="head orange" style="top:196px;left:0;right:0;text-align:center;font-size:34px">Helicopter Tours</div>
    <div style="position:absolute;left:24px;top:240px;display:flex;align-items:center;gap:5px;font-family:'Oswald',sans-serif;font-weight:600;font-size:11px;line-height:1">
      <span style="width:32px;height:32px;border-radius:50%;border:2px solid var(--white);background:#2f6bb3;display:flex;align-items:center;justify-content:center"><svg width="18" height="18"><use href="#i-group"/></svg></span>
      <div>OVER<br><span class="orange" style="font-size:22px">2,000+</span><br>HAPPY FLYERS</div>
    </div>
    <div style="position:absolute;left:148px;top:236px;width:60px;text-align:center;font-family:'Anton',sans-serif;font-size:46px;line-height:1">#1</div>
    <div style="position:absolute;left:218px;top:240px;display:flex;align-items:center;gap:5px;font-family:'Oswald',sans-serif;font-weight:600;font-size:10px;line-height:1.1">
      <span style="width:32px;height:32px;border-radius:50%;border:2px solid var(--white);background:#2f6bb3;display:flex;align-items:center;justify-content:center"><svg width="16" height="16"><use href="#i-thumb"/></svg></span>
      <div>THOUSANDS OF<br><span class="orange" style="font-size:13px">5 STAR REVIEWS</span><br><span class="orange">★★★★★</span></div>
    </div>
    <div style="position:absolute;left:12px;right:12px;top:315px;height:28px;background:var(--navy-glass);border:1px solid #3c78c0;border-radius:4px;text-align:center;font-family:'Oswald',sans-serif;font-weight:700;font-style:italic;font-size:16px;line-height:26px">FLORIDA’S <span class="orange">#1</span> HELICOPTER EXPERIENCE</div>
    <div style="position:absolute;left:12px;right:12px;top:350px;height:42px;background:var(--navy-glass);border:1px solid #3c78c0;border-radius:4px;display:flex;align-items:center;justify-content:space-around">
      <div class="feat feat--o"><svg><use href="#i-shield"/></svg><div>Safe<br>&amp; reliable</div></div><span class="sep"></span>
      <div class="feat feat--o"><svg><use href="#i-headset"/></svg><div>Expert<br>pilots</div></div><span class="sep"></span>
      <div class="feat feat--o"><svg><use href="#i-camera"/></svg><div>Breathtaking<br>views</div></div><span class="sep"></span>
      <div class="feat feat--o"><svg><use href="#i-heart"/></svg><div>Memories<br>that last</div></div>
    </div>
    <div style="position:absolute;left:12px;right:8px;top:402px;display:flex;align-items:center;justify-content:space-between">
      <div class="locs" style="font-family:'Oswald',sans-serif;font-size:8.5px;gap:5px"><svg><use href="#i-pin"/></svg>Tampa <b>|</b> St Petersburg <b>|</b> Sarasota</div>
      <div style="background:var(--orange);border-radius:3px;padding:6px 8px;display:flex;align-items:center;gap:5px;font-family:'Oswald',sans-serif;font-weight:600;font-size:9px"><svg width="11" height="11"><use href="#i-cal"/></svg>BOOK YOUR ADVENTURE TODAY!</div>
    </div>
  </section>

</main>
</body>
</html>
```